LABEL DESIGN for our Hemp oil extract headache relief roll on

We need a pure, elegant and natural label design for our new product from Velmora CBD. We make natural and hand made products with CBD oil & other essential oils to improve wellness being. We would like to see natural, earthy and nice labels.

Target Market(s)

Gender: Feminine

Font styles to use
Serif
Sans Serif
Script

Colors
eea4c8
ffffff
b7a5cd
cadf82
7f7f7f

Requirements
Must have
• Measures of the label should be 2.35 x 2 inches.
Nice to have
• Herb leafs
Should not have
• Marijuana leafs

```html
<!DOCTYPE html>
<html lang="en">
<head>
<meta charset="utf-8">
<title>Velmora CBD – Calm Hours Roll On Label</title>
<link rel="stylesheet" href="https://fonts.googleapis.com/css2?family=Pinyon+Script&family=Open+Sans:wght@400;600&family=Raleway:wght@700&display=swap">
<style>
  :root {
    --leaf-green: #8cc63f;
    --leaf-green-soft: #cadf82;
    --ink-grey: #4a4a4a;
    --paper: #ffffff;
  }
  * { box-sizing: border-box; margin: 0; padding: 0; }
  html, body { width: 800px; height: 1200px; overflow: hidden; background: var(--paper); }
  .canvas { position: relative; width: 800px; height: 1200px; background: var(--paper); }

  .label { position: absolute; left: 0; width: 800px; height: 600px; display: flex; flex-direction: column; align-items: center; }
  .label--front { top: 0; padding-top: 60px; }
  .label--back { top: 600px; padding-top: 40px; }

  .brand { font-family: "Raleway", sans-serif; font-weight: 700; font-size: 26px; letter-spacing: 8px; color: var(--leaf-green); text-align: center; }

  .wreath-area { position: relative; width: 360px; height: 340px; margin-top: 20px; }
  .wreath-art { position: absolute; inset: 0; border-radius: 50%; background: radial-gradient(circle, transparent 56%, var(--leaf-green-soft) 58%, rgba(202,223,130,0.35) 68%, transparent 71%); }
  .wreath-title { position: absolute; inset: 0; display: flex; flex-direction: column; align-items: center; justify-content: center; }

  .product-name { font-family: "Open Sans", sans-serif; font-weight: 600; font-size: 40px; letter-spacing: 3px; color: var(--leaf-green); line-height: 1.1; white-space: nowrap; }
  .product-type { font-family: "Open Sans", sans-serif; font-weight: 600; font-size: 10px; letter-spacing: 1px; color: var(--leaf-green); margin-top: 6px; }
  .tagline { font-family: "Pinyon Script", cursive; font-size: 30px; color: var(--leaf-green); white-space: nowrap; }
  .label--front .tagline { margin-top: 18px; }

  .dose-tag { margin-top: 10px; background: var(--leaf-green); color: var(--paper); font-family: "Open Sans", sans-serif; font-weight: 600; font-size: 22px; padding: 2px 28px; }

  .rose-mark { width: 70px; height: 44px; border-radius: 22px; background: var(--leaf-green-soft); }
  .title-row { display: flex; align-items: center; gap: 14px; margin-top: 14px; }
  .title-band { width: 130px; height: 14px; background: var(--leaf-green-soft); }
  .title-block { display: flex; flex-direction: column; align-items: center; }

  .description { font-family: "Open Sans", sans-serif; font-size: 16px; line-height: 1.45; color: var(--ink-grey); text-align: center; margin-top: 26px; width: 460px; }
  .label--back .tagline { font-size: 24px; margin-top: 14px; }
  .direction-bar { margin-top: 6px; background: var(--leaf-green); color: var(--paper); font-family: "Open Sans", sans-serif; font-size: 13px; padding: 2px 6px; }
  .divider-mark { width: 60px; height: 12px; margin-top: 14px; border-radius: 6px; background: var(--leaf-green-soft); }
  .ingredients { font-family: "Open Sans", sans-serif; font-size: 16px; line-height: 1.6; color: var(--ink-grey); text-align: center; margin-top: 14px; }
  .maker-box { margin-top: 18px; width: 360px; background: var(--leaf-green); color: var(--paper); font-family: "Open Sans", sans-serif; text-align: center; padding: 12px 10px 10px; }
  .maker-box__line { font-size: 16px; line-height: 1.4; }
  .maker-box__web { font-size: 10px; margin-top: 4px; }
</style>
</head>
<body>
<main class="canvas">
  <section class="label label--front">
    <div class="brand">VELMORA CBD</div>
    <div class="wreath-area">
      <div class="wreath-art" role="img" aria-label="Hand-drawn green herb and wildflower wreath"></div>
      <div class="wreath-title">
        <div class="product-name">CALM HOURS</div>
        <div class="product-type">HEMP OIL EXTRACT ROLL ON</div>
      </div>
    </div>
    <div class="tagline">Gentle Comfort, Pure &amp; Simple</div>
    <div class="dose-tag">200mg</div>
  </section>

  <section class="label label--back">
    <div class="rose-mark" role="img" aria-label="Small hand-drawn rose sprig ornament"></div>
    <div class="title-row">
      <div class="title-band" role="img" aria-label="Light green dotted decorative band"></div>
      <div class="title-block">
        <div class="product-name">CALM HOURS</div>
        <div class="product-type">HEMP OIL EXTRACT ROLL ON</div>
      </div>
      <div class="title-band" role="img" aria-label="Light green dotted decorative band"></div>
    </div>
    <p class="description">Natural and therapeuticbalm, made with the finest and purest Hemp from Colorado, know for its healing &amp; restorative properties.</p>
    <div class="tagline">Gentle Comfort, Pure &amp; Simple</div>
    <div class="direction-bar">Direction : Massage into skin. Repeat as needed</div>
    <div class="divider-mark" role="img" aria-label="Small green flourish divider ornament"></div>
    <p class="ingredients">Ingredient : CBD Oil 200mg, rosmery,<br>mint, beeswax, lavanda</p>
    <div class="maker-box">
      <div class="maker-box__line">HECHO POR VELMORA CBD</div>
      <div class="maker-box__line">ASPENFIELD, COLORADO. U . S . A</div>
      <div class="maker-box__web">WWW.VELMORAHEMP.COM</div>
    </div>
  </section>
</main>
</body>
</html>
```